I need a business card design for a new company that will be doing consulting work around issues of cultural competency, and diversity and inclusion. I would like the design to be crisp and clear with bold but conservative colors and incorporate shades of blue

Target Market(s)

Small businesses, schools, non-profits

Industry/Entity Type

Consulting

Font styles to use
Serif
Sans Serif

Colors
0c5ba6
6b449b
3276b5
0292cd

Requirements
Must have
• A Morrow Venture (name of company)
• Lemlem Tavish
• CEO
• lemlem@amorrowventure.com
• (215)483-2756

```html
<!DOCTYPE html>
<html lang="en">
<head>
<meta charset="utf-8">
<title>Lemlem Tavish — A Morrow Venture</title>
<link href="https://fonts.googleapis.com/css2?family=Quicksand:wght@300;400&family=Poppins:wght@400&display=swap" rel="stylesheet">
<style>
  :root {
    --sky-blue: #0292cd;
    --sky-light: #3aa6d8;
    --mid-blue: #1f80c2;
    --steel-blue: #3276b5;
    --royal-purple: #6b449b;
    --purple-shade: #5c3890;
    --ink-white: #ffffff;
  }
  html, body {
    margin: 0;
    padding: 0;
    overflow: hidden;
    background: #ffffff;
  }
  .card {
    position: relative;
    width: 1200px;
    height: 514px;
    overflow: hidden;
    color: var(--ink-white);
  }
  .card-backdrop {
    position: absolute;
    inset: 0;
  }
  .holder-name {
    position: absolute;
    left: 79px;
    top: 166px;
    margin: 0;
    font-family: "Quicksand", sans-serif;
    font-weight: 300;
    font-size: 76px;
    line-height: 1;
    letter-spacing: 0.5px;
  }
  .holder-role {
    position: absolute;
    left: 80px;
    top: 281px;
    margin: 0;
    font-family: "Quicksand", sans-serif;
    font-weight: 300;
    font-size: 32px;
    line-height: 1;
  }
  .contact-heading {
    position: absolute;
    left: 790px;
    width: 328px;
    top: 152px;
    margin: 0;
    padding-bottom: 10px;
    border-bottom: 1.5px solid var(--ink-white);
    text-align: center;
    font-family: "Quicksand", sans-serif;
    font-weight: 400;
    font-size: 34px;
    line-height: 1;
  }
  .contact-list {
    position: absolute;
    left: 772px;
    top: 244px;
    margin: 0;
    padding: 0;
    list-style: none;
  }
  .contact-item {
    display: flex;
    align-items: center;
    height: 44px;
    margin-bottom: 23px;
    font-family: "Poppins", sans-serif;
    font-size: 20px;
  }
  .contact-icon {
    width: 44px;
    height: 44px;
    margin-right: 20px;
    flex: none;
  }
</style>
</head>
<body>
<div class="card">
  <svg class="card-backdrop" width="1200" height="514" viewBox="0 0 1200 514" aria-hidden="true">
    <defs>
      <linearGradient id="sky-wash" x1="0" y1="0" x2="0.5" y2="0.6">
        <stop offset="0" stop-color="var(--sky-light)"/>
        <stop offset="0.35" stop-color="var(--sky-blue)"/>
        <stop offset="1" stop-color="var(--sky-blue)"/>
      </linearGradient>
      <linearGradient id="purple-edge" x1="0" y1="0" x2="1" y2="0">
        <stop offset="0" stop-color="var(--purple-shade)"/>
        <stop offset="0.12" stop-color="var(--royal-purple)"/>
        <stop offset="1" stop-color="var(--royal-purple)"/>
      </linearGradient>
    </defs>
    <rect class="sky-field" width="1200" height="514" fill="url(#sky-wash)"/>
    <polygon class="band-mid" points="641,0 1200,0 1200,514 557,514" fill="var(--mid-blue)"/>
    <polygon class="band-steel" points="693,0 1200,0 1200,514 605,514" fill="var(--steel-blue)"/>
    <polygon class="purple-panel" points="737,0 1200,0 1200,514 638,514" fill="url(#purple-edge)"/>
  </svg>

  <h1 class="holder-name">Lemlem Tavish</h1>
  <p class="holder-role">CEO</p>

  <h2 class="contact-heading">Contact Information</h2>
  <ul class="contact-list">
    <li class="contact-item">
      <svg class="contact-icon" viewBox="0 0 44 44" fill="none" stroke="#ffffff" stroke-width="1.8" aria-hidden="true">
        <circle cx="22" cy="22" r="20"/>
        <ellipse cx="22" cy="22" rx="9" ry="20"/>
        <line x1="22" y1="2" x2="22" y2="42"/>
        <line x1="2" y1="22" x2="42" y2="22"/>
        <path d="M5 12 H39 M5 32 H39"/>
      </svg>
      <span class="contact-email">lemlem@amorrowventure.com</span>
    </li>
    <li class="contact-item">
      <svg class="contact-icon" viewBox="0 0 44 44" fill="none" stroke="#ffffff" stroke-width="1.8" stroke-linejoin="round" aria-hidden="true">
        <path d="M9 3 L15 3 L19 13 L14 17 C16 24 20 28 27 30 L31 25 L41 29 L41 35 C41 39 38 42 34 41 C18 38 6 26 3 10 C2 6 5 3 9 3 Z"/>
      </svg>
      <span class="contact-phone">(215)483-2756</span>
    </li>
  </ul>
</div>
</body>
</html>
```